Velliora Events Business Card

We need a business cards that stands out to our clients. We are company who targets prestige clients to spend money with us on experiences, so our image needs to be prestige
Target Market(s)
Corporate
Contact Information for Business Card
There will be four different names on the business cards
Danielle Brontoss
Director
O: 02 5174 2038
M: 0491 652 083
E: info@vellioraevents.example.com.au
Facebook: @vellioraevents
Instagram: vellioraevents
www.vellioraevents.example.com.au
Nathaniel Brontoss
Director
O: 02 5174 2038
M: 0478 205 946
Facebook: @vellioraevents
Instagram: vellioraevents
www.vellioraevents.example.com.au
Elias Dorvek
Director
O: 02 5174 2038
M: 0467 319 752
Facebook: @vellioraevents
Instagram: vellioraevents
www.vellioraevents.example.com.au
Marta Quell
Director
O: 02 5174 2038
Facebook: @vellioraevents
Instagram: vellioraevents
www.vellioraevents.example.com.au
Colors
Designer to choose colors to be used in the design.
Look and feel

```html
<!DOCTYPE html>
<html lang="en">
<head>
<meta charset="utf-8">
<title>Velliora Events – Business Card</title>
<link rel="stylesheet" href="https://fonts.googleapis.com/css2?family=Cinzel:wght@700&family=Lora:wght@400&display=swap">
<style>
  :root {
    --backdrop: #1b1b1d;
    --navy: #23214f;
    --gold: #d4b15e;
    --gold-light: #f3dc8a;
    --gold-dark: #a8832f;
    --paper-text: #e9e6f2;
  }
  * { margin: 0; padding: 0; box-sizing: border-box; }
  html, body {
    width: 1200px; height: 852px; overflow: hidden;
    background: var(--backdrop);
  }
  .canvas { position: relative; width: 1200px; height: 852px; }

  .card {
    position: absolute;
    width: 500px; height: 286px;
    border-radius: 18px;
    background: var(--navy);
    overflow: hidden;
    box-shadow: 0 10px 30px rgba(0,0,0,.45);
  }
  .card--front { left: 130px; top: 120px; }
  .card--back  { left: 570px; top: 446px; }

  .brand-name {
    position: absolute;
    font-family: "Lora", serif;
    font-weight: 400;
    text-align: center;
    line-height: 1.2;
    white-space: nowrap;
  }
  .card--front .brand-name {
    left: 0; right: 0; top: 112px;
    font-size: 34px;
    color: var(--gold);
  }
  .card--back .brand-name {
    left: 318px; width: 182px; top: 128px;
    font-size: 21px;
    color: var(--navy);
  }

  .socials {
    position: absolute; left: 0; right: 0; bottom: 30px;
    display: flex; justify-content: center; gap: 22px;
    font-family: "Lora", serif; font-size: 12.5px; color: var(--paper-text);
  }
  .socials__item { display: flex; align-items: center; gap: 7px; }
  .socials__dot {
    width: 13px; height: 13px; border-radius: 50%;
    background: var(--gold);
  }

  .gold-panel { position: absolute; inset: 0; }

  .person { position: absolute; left: 32px; top: 62px; }
  .person__name {
    font-family: "Cinzel", serif; font-weight: 700;
    font-size: 16px; letter-spacing: .06em;
    color: var(--gold);
  }
  .person__role {
    font-family: "Lora", serif; font-size: 11.5px;
    color: var(--paper-text); margin-top: 4px;
  }

  .contacts {
    position: absolute; left: 32px; bottom: 24px;
    list-style: none;
    font-family: "Lora", serif; font-size: 12.5px; color: var(--paper-text);
  }
  .contacts__item { display: flex; align-items: center; gap: 12px; margin-top: 5px; }
  .contacts__icon { width: 13px; height: 13px; flex: none; }
</style>
</head>
<body>
<main class="canvas">

  <section class="card card--front" aria-label="Business card front">
    <div class="brand-name">Velliora Events</div>
    <div class="socials">
      <span class="socials__item"><span class="socials__dot"></span>@vellioraevents</span>
      <span class="socials__item"><span class="socials__dot"></span>vellioraevents</span>
    </div>
  </section>

  <section class="card card--back" aria-label="Business card back">
    <svg class="gold-panel" viewBox="0 0 500 286" width="500" height="286" aria-hidden="true">
      <defs>
        <linearGradient id="goldSheen" x1="0" y1="0" x2="1" y2="1">
          <stop offset="0" stop-color="var(--gold-dark)"/>
          <stop offset=".35" stop-color="var(--gold-light)"/>
          <stop offset=".6" stop-color="var(--gold)"/>
          <stop offset="1" stop-color="var(--gold-dark)"/>
        </linearGradient>
      </defs>
      <path d="M300,0 C258,110 288,222 372,286 L500,286 L500,0 Z" fill="url(#goldSheen)"/>
    </svg>

    <div class="brand-name">Velliora Events</div>

    <div class="person">
      <div class="person__name">DANIELLE BRONTOSS</div>
      <div class="person__role">Director</div>
    </div>

    <ul class="contacts">
      <li class="contacts__item">
        <svg class="contacts__icon" viewBox="0 0 14 14"><path d="M3 1.5 L5.5 1.5 L6.5 4.5 L5 5.6 C5.8 7.3 6.8 8.3 8.4 9 L9.5 7.5 L12.5 8.5 L12.5 11 C12.5 12 11.8 12.6 10.8 12.5 C5.8 12 2 8.2 1.5 3.2 C1.4 2.2 2 1.5 3 1.5 Z" fill="none" stroke="var(--gold)" stroke-width="1.2"/></svg>
        02 5174 2038
      </li>
      <li class="contacts__item">
        <svg class="contacts__icon" viewBox="0 0 14 14"><rect x="3.5" y="1" width="7" height="12" rx="1.5" fill="none" stroke="var(--gold)" stroke-width="1.4"/><circle cx="7" cy="10.6" r=".9" fill="var(--gold)"/></svg>
        0491 652 083
      </li>
      <li class="contacts__item">
        <svg class="contacts__icon" viewBox="0 0 14 14"><rect x="1" y="3" width="12" height="8.5" rx="1" fill="none" stroke="var(--gold)" stroke-width="1.4"/><path d="M1.5 3.5 L7 8 L12.5 3.5" fill="none" stroke="var(--gold)" stroke-width="1.4"/></svg>
        info@vellioraevents.example.com.au
      </li>
      <li class="contacts__item">
        <svg class="contacts__icon" viewBox="0 0 14 14"><circle cx="7" cy="7" r="5.8" fill="none" stroke="var(--gold)" stroke-width="1.3"/><ellipse cx="7" cy="7" rx="2.5" ry="5.8" fill="none" stroke="var(--gold)" stroke-width="1"/><path d="M1.2 7 H12.8" stroke="var(--gold)" stroke-width="1"/></svg>
        www.vellioraevents.example.com.au
      </li>
    </ul>
  </section>

</main>
</body>
</html>
```